Cover für Hauptkatalog
Zielgruppe
TESSARIN GmbH ist ein führender Großhändler in der Hobby- und Bastelbranche. mit unseren weit über 8.000 Produkten beliefern wir Einzelhändler in ganz Europa. Durch unsere Größe sind wir in der Lage sehr schnell auf individuelle Kundenwünsche zu reagieren.
Aufgabenstellung
Wir werden Mitte Dezember einen neuen Kreativ-Katalog mit über 450 Seiten unseren Kunden zur Verfügung stellen. In diesem Zusammenhang soll der Umschlag (Vorder- und Rückseite) in einem neuen, frischen Design erscheinen. Das aktuelle Layout kann unter www.tessarin-hobby.example eingesehen werden. Auf der Rückseite soll unsere Adresse stehen.

```html
<!DOCTYPE html>
<html lang="de">
<head>
<meta charset="utf-8">
<title>Tessarin Katalog – Rückseite</title>
<link href="https://fonts.googleapis.com/css2?family=Lato:wght@300;400;700;900&display=swap" rel="stylesheet">
<style>
  :root{
    --brand-blue:#243a8e;
    --band-blue:#2a3f8f;
    --brand-red:#d63a2b;
    --paper:#ffffff;
    --frame:#ffffff;
  }
  *{margin:0;padding:0;box-sizing:border-box;}
  html,body{width:1200px;height:850px;overflow:hidden;background:var(--paper);}
  .cover{position:relative;width:1200px;height:850px;background:var(--paper);font-family:'Lato',sans-serif;color:var(--brand-blue);}
  .rule-top{position:absolute;left:0;top:0;width:1200px;height:2px;background:#c9c9c9;}
  .stripe{position:absolute;left:0;width:1200px;height:6px;background:var(--brand-red);}
  .stripe--upper{top:31px;}
  .stripe--lower{top:464px;}
  .photo-band{position:absolute;left:0;top:37px;width:1200px;height:427px;background:var(--band-blue);}
  .photo{position:absolute;width:274px;height:194px;background:var(--frame);padding:5.5px;}
  .photo span{display:block;width:100%;height:100%;}
  .c1{left:27.5px}.c2{left:309.5px}.c3{left:616px}.c4{left:902px}
  .r1{top:16.6px}.r2{top:218px}

  .wordmark{position:absolute;font-weight:900;color:var(--brand-blue);letter-spacing:-1px;display:flex;align-items:center;gap:8px;}
  .wordmark::after{content:"";display:block;background:var(--brand-red);}
  .wordmark--small{left:42px;top:494px;font-size:44px;}
  .wordmark--small::after{width:30px;height:30px;}
  .wordmark--large{right:33px;top:735px;font-size:62px;}
  .wordmark--large::after{width:42px;height:42px;}

  .info{position:absolute;left:42px;top:573px;font-weight:300;font-size:15.5px;line-height:19.5px;}
  .address{position:absolute;top:662px;font-weight:300;font-size:17.5px;line-height:20.2px;font-style:normal;}
  .address strong{font-weight:400;}
  .address--ch{left:42px;}
  .address--de{left:290px;}
  .website{position:absolute;left:42px;top:788px;font-weight:300;font-size:35px;}

  .slogan{position:absolute;right:30px;text-align:right;font-weight:300;white-space:nowrap;}
  .slogan--de{top:482px;font-size:58px;}
  .slogan--fr{top:551px;font-size:44px;}
  .slogan--en{top:604px;font-size:44px;}
</style>
</head>
<body>
<main class="cover">
  <div class="rule-top"></div>
  <div class="stripe stripe--upper"></div>
  <section class="photo-band">
    <figure class="photo c1 r1"><span role="img" aria-label="Festlicher Tisch mit bemalter Kerze, Cupcakes und Gläsern" style="background:linear-gradient(135deg,#cfe6ef,#f4f1ec 55%,#a9d4e4)"></span></figure>
    <figure class="photo c2 r1"><span role="img" aria-label="Dekorierte türkisfarbene Eulenfigur mit Strasssteinen und Windlichtern" style="background:linear-gradient(135deg,#f3eef2,#5fb3d6 50%,#e69ac0)"></span></figure>
    <figure class="photo c3 r1"><span role="img" aria-label="Bunte Papierblumen auf Stäben im Garten" style="background:linear-gradient(135deg,#6f9a4a,#e6a3c8 45%,#e8d84a 70%,#4f7a33)"></span></figure>
    <figure class="photo c4 r1"><span role="img" aria-label="Farbige Windräder mit Ornamentmuster" style="background:linear-gradient(135deg,#b58ad0,#f08a3a 40%,#f1e05a 65%,#6fa0dc)"></span></figure>
    <figure class="photo c1 r2"><span role="img" aria-label="Blau strukturierte Gefässe mit grünen Äpfeln" style="background:linear-gradient(135deg,#3f7fd0,#a8cfe8 50%,#a9cf5a)"></span></figure>
    <figure class="photo c2 r2"><span role="img" aria-label="Nahaufnahme bunter Windräder" style="background:linear-gradient(135deg,#f08a3a,#e85aa6 50%,#6fa8e0)"></span></figure>
    <figure class="photo c3 r2"><span role="img" aria-label="Blaue Schale und Becher mit Äpfeln auf einem Tisch" style="background:linear-gradient(135deg,#4d7a3a,#7fb6e0 45%,#e9eef0 70%,#9cc64e)"></span></figure>
    <figure class="photo c4 r2"><span role="img" aria-label="Gelbe und grüne Glasperlenketten mit Band" style="background:linear-gradient(135deg,#eef6d0,#d8e84a 50%,#3fa04a)"></span></figure>
  </section>
  <div class="stripe stripe--lower"></div>

  <div class="wordmark wordmark--small">TESSARIN</div>

  <p class="info">Weitere Informationen und Bezugsquellennachweis<br>Pour toute information complementaire et liste de revendeurs<br>Further information and documentation can be obtained from</p>

  <address class="address address--ch"><strong>TESSARIN AG</strong><br>Lindenweg 8<br>CH-4400 Mattenbach<br>Phone: +41 61 555 01 20<br>Fax: +41 61 555 01 29<br>info@tessarin.example</address>
  <address class="address address--de"><strong>TESSARIN GmbH</strong><br>Brunnenstrasse 23<br>D-79600 Talheim<br>Phone: +49 7600 5550 0<br>Fax: +49 7600 5559<br>kontakt@tessarin-hobby.example</address>

  <p class="website">www.tessarin-hobby.example</p>

  <h1 class="slogan slogan--de">Freude an Kreativität</h1>
  <p class="slogan slogan--fr">Plaisir de créer</p>
  <p class="slogan slogan--en">Creative pleasure</p>

  <div class="wordmark wordmark--large">TESSARIN</div>
</main>
</body>
</html>
```